Travel Blogger Business Card for roamquill.net

I need a two-sided business card for a travel blogging website. The card should be both professional and fun at the same time. This is for the website www.roamquill.net

I don't necessarily think that the current logo on the website needs to be used on the business card but it can be. I am very flexible with ideas

Target Market(s)

Travel agencies that will be met at a conference.

Industry/Entity Type

Travel

Contact Information for Business Card

Company Name: Roam Quill.net
Name: Bertrand Olesky
Voice: +1-(345)-402-7731
Address: Coral Reach Shore, Grand Cayman, Cayman Islands
Email: ceo@roamquill.net

Colors
0592cd
0355a3
3176b5
33a6d7
85cae6
85acd3

Requirements
Must have
• Website address and name should be bigger than address, phone number, and email.

```html
<!DOCTYPE html>
<html lang="en">
<head>
<meta charset="utf-8">
<title>Roam Quill – Business Card</title>
<link rel="stylesheet" href="https://fonts.googleapis.com/css2?family=Roboto:wght@400;500;700&family=Archivo:wght@800&display=swap">
<style>
  :root {
    --stage: #e4e6e8;
    --teal-light: #5fa3b3;
    --teal: #4a8c9e;
    --teal-deep: #2c6d80;
    --teal-faint: rgba(255, 255, 255, 0.08);
    --ink: #3a3d40;
    --ink-soft: #55595d;
    --paper: #ffffff;
    --name: #2f6f85;
  }
  * { box-sizing: border-box; margin: 0; padding: 0; }
  html, body { width: 1200px; height: 852px; overflow: hidden; }
  body {
    background: var(--stage);
    font-family: "Roboto", Arial, sans-serif;
    display: flex;
    align-items: center;
    justify-content: center;
    gap: 40px;
  }
  .card {
    width: 520px;
    height: 300px;
    border-radius: 16px;
    position: relative;
    overflow: hidden;
    box-shadow: 0 6px 18px rgba(0, 0, 0, 0.18);
  }

  /* Front */
  .card--front {
    background: linear-gradient(160deg, var(--teal-light) 0%, var(--teal) 50%, var(--teal-deep) 100%);
  }
  .front__map {
    position: absolute;
    left: 60px;
    top: 40px;
    width: 400px;
    height: 220px;
    border-radius: 24px;
    background: radial-gradient(ellipse at center, var(--teal-faint) 0%, rgba(255,255,255,0.03) 65%, transparent 100%);
  }
  .front__brand {
    position: absolute;
    inset: 0;
    display: flex;
    align-items: center;
    justify-content: center;
    gap: 14px;
  }
  .brand-dot {
    width: 40px;
    height: 40px;
    border-radius: 50%;
    background: var(--paper);
  }
  .front__name {
    font-family: "Archivo", Arial, sans-serif;
    font-weight: 800;
    font-size: 34px;
    letter-spacing: 0.5px;
    color: var(--paper);
  }

  /* Back */
  .card--back { background: var(--paper); }
  .back__figure {
    position: absolute;
    right: 0;
    top: 0;
    width: 270px;
    height: 200px;
    background: linear-gradient(90deg, rgba(95, 163, 179, 0) 0%, rgba(95, 163, 179, 0.55) 45%, var(--teal) 100%);
  }
  .back__brand {
    position: absolute;
    left: 30px;
    top: 58px;
    font-family: "Archivo", Arial, sans-serif;
    font-weight: 800;
    font-size: 30px;
    color: var(--ink);
  }
  .person {
    position: absolute;
    left: 30px;
    top: 148px;
  }
  .person__name {
    font-weight: 700;
    font-size: 20px;
    color: var(--name);
  }
  .person__role {
    font-size: 11px;
    color: var(--ink-soft);
    margin-top: 2px;
  }
  .contacts {
    position: absolute;
    left: 30px;
    top: 202px;
    list-style: none;
    font-size: 12px;
    color: var(--ink);
    line-height: 1.5;
  }
  .contacts li { display: flex; align-items: center; gap: 8px; }
  .contacts svg { width: 11px; height: 11px; fill: var(--ink); flex: none; }
  .contacts .website { font-size: 15px; font-weight: 500; color: var(--name); }
  .contacts .website svg { fill: var(--name); }
  .contacts .address { padding-left: 19px; }
</style>
</head>
<body>
  <section class="card card--front">
    <div class="front__map" role="img" aria-label="Faint world map across the card"></div>
    <div class="front__brand">
      <span class="brand-dot"></span>
      <span class="front__name">ROAM QUILL</span>
    </div>
  </section>

  <section class="card card--back">
    <div class="back__figure" role="img" aria-label="Large teal silhouette of a camel being led"></div>
    <div class="back__brand">ROAM QUILL</div>
    <div class="person">
      <div class="person__name">Bertrand Olesky</div>
      <div class="person__role">Managing Director</div>
    </div>
    <ul class="contacts">
      <li>
        <svg viewBox="0 0 16 16" aria-hidden="true"><path d="M3 1h3l1.5 4-2 1.2a9 9 0 0 0 4.3 4.3L11 8.5l4 1.5v3a2 2 0 0 1-2 2A12 12 0 0 1 1 3a2 2 0 0 1 2-2z"/></svg>
        +1-(345)-402-7731
      </li>
      <li>
        <svg viewBox="0 0 16 16" aria-hidden="true"><path d="M1 3h14v10H1z M1 3l7 6 7-6" fill="none" stroke="#3a3d40" stroke-width="1.6"/></svg>
        ceo@roamquill.net
      </li>
      <li class="website">
        <svg viewBox="0 0 16 16" aria-hidden="true"><circle cx="8" cy="8" r="7"/><path d="M1 8h14M8 1c-3 3-3 11 0 14M8 1c3 3 3 11 0 14" fill="none" stroke="#fff" stroke-width="1"/></svg>
        www.roamquill.net
      </li>
      <li class="address">Coral Reach Shore, Grand Cayman, Cayman Islands</li>
    </ul>
  </section>
</body>
</html>
```